French Puns

Creation of a cover for a book on French plays on words.
The public is lovers of the French language
TITLE: The small voices of Lucien Marbois
SUB-TITLE: Playful words, words at play
PUBLISHER (at the bottom of the page): Editions Corvane
(See joined examples, previous books of the same author)
Size: 14 x 20.5 cm
Please note that the text on the cover is in French, not in English:
Small voices from Lucien Marbois
Witty words, witty words (subtitle, smaller)
Corvane Editions

```html
<!DOCTYPE html>
<html lang="en">
<head>
<meta charset="utf-8">
<title>The small voices of Lucien Marbois — Book cover</title>
<link href="https://fonts.googleapis.com/css2?family=Fredoka:wght@600&family=Quicksand:wght@500&family=Handlee&display=swap" rel="stylesheet">
<style>
  :root {
    --paper: #ffffff;
    --ink: #1a1a1a;
    --wine: #a91f27;
    --edge: #111111;
  }
  * { margin: 0; padding: 0; box-sizing: border-box; }
  html, body {
    width: 1200px;
    height: 1200px;
    overflow: hidden;
    background: var(--paper);
  }
  .canvas {
    position: relative;
    width: 1200px;
    height: 1200px;
  }
  .cover {
    position: absolute;
    left: 289px;
    top: 136px;
    width: 607px;
    height: 888px;
    background: var(--paper);
    border: 1.5px solid var(--edge);
    text-align: center;
  }
  .cover__lead {
    position: absolute;
    top: 196px;
    left: 0;
    right: 0;
    font-family: "Quicksand", sans-serif;
    font-weight: 500;
    font-size: 31px;
    color: var(--ink);
    letter-spacing: 0.2px;
  }
  .cover__author {
    position: absolute;
    top: 268px;
    left: 0;
    right: 0;
    font-family: "Fredoka", sans-serif;
    font-weight: 600;
    font-size: 104px;
    line-height: 120px;
    color: var(--wine);
    letter-spacing: 4px;
    text-transform: uppercase;
  }
  .cover__author span { display: block; }
  .cover__subtitle {
    position: absolute;
    top: 548px;
    left: 0;
    right: 0;
    font-family: "Handlee", cursive;
    font-size: 36px;
    line-height: 54px;
    color: var(--wine);
  }
  .cover__subtitle span { display: block; }
  .cover__publisher {
    position: absolute;
    top: 828px;
    left: 0;
    right: 0;
    font-family: "Quicksand", sans-serif;
    font-weight: 500;
    font-size: 19px;
    color: var(--ink);
  }
</style>
</head>
<body>
  <main class="canvas">
    <article class="cover">
      <p class="cover__lead">The small voices of</p>
      <h1 class="cover__author"><span>Lucien</span><span>Marbois</span></h1>
      <p class="cover__subtitle"><span>Playful words,</span><span>words at play</span></p>
      <p class="cover__publisher">Editions Corvane</p>
    </article>
  </main>
</body>
</html>
```